Design our branded business card!

We'd love for you to design our business card and come up with a fitting design that reflects the Pivex brand. We're a growing tech startup with big ambitions. We've included our brand guidelines (contain colour palette), logo (EPS vector in CMYK) and old designs to help you on your way.

We'd like to keep the design fairly simple:

* Name
* Phone number
* Email address
* Website (www.pivex.life)
* Twitter (@pivex)
* Address (18 Wexham Row, Leeds, UK, LS9 4ZQ).

This would need to include print and cutting marks.

If you have any questions just let us know!

Target Market(s)

Businesses, Press and our customers!

Industry/Entity Type

Business

Contact Information for Business Card

* Name
* Phone number
* Email address
* Twitter (@pivex)

Font styles to use
Sans Serif

Requirements
Must have
• 1. Must have the Pivex logo included.
• 2. Must use the font 'Brandon Text' in either 'light' or 'thin' (https://www.typevault-demo.com/fonts/qrsfonts/halden-sans/)
• 3. Must use exact colours references from the brand guidelines. Colours outside of the brand guidelines will be discounted. White (transparent) backgrounds are fine.
• 4. Must contain the following information:
• * Name
• * Phone number
• * Email address
• * Website (www.pivex.life)
• * Twitter (@pivex)
• * Address (18 Wexham Row, Leeds, UK, LS9 4ZQ).
Nice to have
• Must use the font 'Brandon Text' in either 'light' or 'thin' (https://www.typevault-demo.com/fonts/qrsfonts/halden-sans/)
Should not have
• Colours outside of the brand guidelines will be discounted. White (transparent) backgrounds are fine.
• Avoid creating icons or including photography.

```html
<!DOCTYPE html>
<html lang="en">
<head>
<meta charset="utf-8">
<title>Pivex business card</title>
<link href="https://fonts.googleapis.com/css2?family=Raleway:wght@300;400&display=swap" rel="stylesheet">
<style>
  :root {
    --brand-green: #6ab45f;
    --brand-green-light: #7cc272;
    --brand-green-pale: #a9dba1;
    --ink: #333333;
    --paper: #ffffff;
    --mist: #e4e2e3;
    --backdrop: #eceeee;
  }
  * { box-sizing: border-box; margin: 0; padding: 0; }
  html, body { width: 1200px; height: 900px; overflow: hidden; }
  body {
    background: var(--backdrop);
    font-family: "Raleway", sans-serif;
    font-weight: 300;
    position: relative;
  }
  .card {
    position: absolute;
    top: 292px;
    width: 540px;
    height: 316px;
    overflow: hidden;
    box-shadow: 0 2px 6px rgba(0,0,0,0.12);
  }
  .card--front { left: 40px; background: var(--brand-green-light); }
  .card--back { left: 620px; background: var(--paper); }

  .wordmark {
    position: absolute;
    display: flex;
    align-items: center;
    gap: 18px;
    font-weight: 300;
    letter-spacing: 1px;
    line-height: 1;
  }
  .wordmark__dot { border-radius: 50%; flex: none; }
  .card--front .wordmark { left: 92px; top: 92px; color: var(--paper); font-size: 68px; }
  .card--front .wordmark__dot { width: 70px; height: 70px; background: var(--paper); }
  .card--back .wordmark { left: 150px; top: 56px; color: var(--ink); font-size: 60px; }
  .card--back .wordmark__dot { width: 62px; height: 62px; background: var(--brand-green); }

  .band { position: absolute; left: 0; width: 100%; }
  .front-rule-top { top: 212px; height: 12px; background: var(--paper); }
  .front-rule-bottom { top: 262px; height: 12px; background: var(--paper); }
  .front-site {
    position: absolute; top: 232px; right: 34px;
    color: var(--brand-green-pale);
    font-size: 15px; letter-spacing: 9px;
  }

  .back-halo {
    position: absolute; left: 40px; top: 120px;
    width: 230px; height: 230px; border-radius: 50%;
    background: var(--mist);
  }
  .contact-name {
    position: absolute; left: 40px; top: 160px;
    font-size: 24px; color: var(--ink); font-weight: 400;
  }
  .contact-address {
    position: absolute; left: 40px; top: 192px;
    font-size: 12px; color: var(--ink); letter-spacing: .5px;
  }
  .back-rule { top: 218px; height: 3px; background: var(--brand-green); }
  .back-bar { height: 24px; background: var(--brand-green); color: var(--paper);
    display: flex; align-items: center; justify-content: space-between;
    padding: 0 22px 0 40px; font-size: 12.5px; letter-spacing: .4px; }
  .back-bar--one { top: 226px; }
  .back-bar--two { top: 254px; }
  .back-bar--three { top: 282px; }
  .item { display: flex; align-items: center; gap: 8px; }
  .item svg { width: 16px; height: 16px; flex: none; }
  .social-dot { width: 12px; height: 12px; border-radius: 50%; background: var(--paper); }
</style>
</head>
<body>
  <section class="card card--front" aria-label="Card front">
    <div class="wordmark"><span class="wordmark__dot"></span><span>pivex</span></div>
    <div class="band front-rule-top"></div>
    <p class="front-site">www.pivex.life</p>
    <div class="band front-rule-bottom"></div>
  </section>

  <section class="card card--back" aria-label="Card back">
    <div class="back-halo"></div>
    <div class="wordmark"><span class="wordmark__dot"></span><span>pivex</span></div>
    <p class="contact-name">Name</p>
    <p class="contact-address">18 Wexham Row, Leeds, UK, LS9 4ZQ</p>
    <div class="band back-rule"></div>
    <div class="band back-bar back-bar--one">
      <span></span>
      <span class="item"><span class="social-dot"></span>@pivex</span>
    </div>
    <div class="band back-bar back-bar--two">
      <span class="item">
        <svg viewBox="0 0 16 16" fill="none" stroke="#fff" stroke-width="1.2"><path d="M2 6c0-2 2-3 6-3s6 1 6 3v1h-3V5.5H5V7H2z"/><rect x="3" y="8" width="10" height="6" rx="1"/><circle cx="8" cy="11" r="1.6"/></svg>
        111-1111-1111
      </span>
      <span class="item">
        <svg viewBox="0 0 16 16" fill="none" stroke="#fff" stroke-width="1.1"><circle cx="8" cy="8" r="6.5"/><ellipse cx="8" cy="8" rx="3" ry="6.5"/><path d="M1.5 8h13M3 4.5h10M3 11.5h10"/></svg>
        www.pivex.life
      </span>
    </div>
    <div class="band back-bar back-bar--three">
      <span class="item">
        <svg viewBox="0 0 16 16" fill="none" stroke="#fff" stroke-width="1.2"><rect x="1.5" y="3.5" width="13" height="9"/><path d="M1.5 3.5 8 9l6.5-5.5"/></svg>
        email@email.com
      </span>
      <span></span>
    </div>
  </section>
</body>
</html>
```